Visitenkarten-Design für Maler
Zielgruppe
Ausführung von Malerarbeiten,Innenraumgestaltung
Aufgabenstellung
Stichworte :Eilaufträge Seniorenservice Kleinaufträge

```html
<!DOCTYPE html>
<html lang="de">
<head>
<meta charset="utf-8">
<title>Visitenkarte Malerfachbetrieb Jonas Brenner</title>
<link href="https://fonts.googleapis.com/css2?family=Lato:wght@400;700;900&display=swap" rel="stylesheet">
<style>
  :root {
    --bg: #eeeeee;
    --card: #ffffff;
    --ink: #5a5a5a;
    --ink-strong: #555555;
    --accent-red: #e2001a;
    --shadow: rgba(0, 0, 0, 0.12);
  }
  html, body {
    margin: 0;
    padding: 0;
    width: 1200px;
    height: 864px;
    overflow: hidden;
    background: var(--bg);
    font-family: "Lato", Arial, sans-serif;
  }
  .stage {
    width: 1200px;
    height: 864px;
    display: flex;
    align-items: center;
    justify-content: center;
    gap: 48px;
  }
  .card {
    position: relative;
    width: 520px;
    height: 336px;
    background: var(--card);
    box-shadow: 0 10px 28px var(--shadow);
    box-sizing: border-box;
  }
  /* front side */
  .card--front .brand {
    position: absolute;
    left: 150px;
    top: 92px;
    display: flex;
    align-items: center;
    gap: 14px;
  }
  .brand__mark {
    width: 22px;
    height: 22px;
    background: var(--accent-red);
  }
  .brand__name {
    font-weight: 900;
    color: var(--ink-strong);
    font-size: 27px;
    line-height: 1.05;
  }
  .card--front .services {
    position: absolute;
    left: 56px;
    right: 40px;
    top: 200px;
    font-weight: 700;
    font-size: 14px;
    color: var(--ink);
    text-align: center;
  }
  .card--front .mobile {
    position: absolute;
    left: 56px;
    right: 40px;
    top: 228px;
    font-size: 14px;
    color: var(--ink);
    text-align: center;
  }
  /* back side */
  .card--back .accent {
    position: absolute;
    left: 60px;
    top: 60px;
    width: 22px;
    height: 22px;
    background: var(--accent-red);
  }
  .card--back .contact {
    position: absolute;
    left: 150px;
    top: 118px;
    margin: 0;
    padding: 0;
    list-style: none;
    font-size: 14px;
    line-height: 1.75;
    color: var(--ink);
  }
</style>
</head>
<body>
  <main class="stage">
    <section class="card card--front" aria-label="Vorderseite">
      <div class="brand">
        <span class="brand__mark"></span>
        <span class="brand__name">Malerfachbetrieb<br>Jonas Brenner</span>
      </div>
      <p class="services">Eilaufträge / Seniorenservice / Kleinaufträge</p>
      <p class="mobile">Mobil: 0160/52384017</p>
    </section>

    <section class="card card--back" aria-label="Rückseite">
      <span class="accent"></span>
      <ul class="contact">
        <li>Tel. 030/41870236</li>
        <li>www.malerbetrieb-jonas-brenner.de</li>
        <li>E-Mail: info@malerbetrieb-jonas-brenner.de</li>
      </ul>
    </section>
  </main>
</body>
</html>
```